2nd Generation Blind Manufacturer & Retailer Needs A Stationary Set

We need a stationary set for a family business located the in the Whitsundays (QLD). We retail and manufacture blinds awnings and shutters. Second generation, in operation for over 30 years.

Final draft must include at minimum:

Business Card (2 Sided)
Letterhead
Presentation Folder

Target Market(s)

home owners, landlords, builders, real estate agents, shopping centres

Industry/Entity Type

Textile

Requirements
Must have
• Design needs to work in mono as well as colour print
Nice to have
• Relevant to the textile industry
Should not have
• The inclusion of blinds, awnings or shutters is an automatic no-no

```html
<!DOCTYPE html>
<html lang="en">
<head>
<meta charset="utf-8">
<title>Harbrook Blinds — Stationery Set</title>
<link href="https://fonts.googleapis.com/css2?family=Questrial&display=swap" rel="stylesheet">
<style>
  :root {
    --backdrop: #cfcfcf;
    --folder: #6b6b6b;
    --folder-spine: #626262;
    --folder-mark: #767676;
    --paper: #f0f0f0;
    --ink: #4a4a4a;
    --ink-soft: #6f6f6f;
    --rule-light: #a9a9a9;
    --rule-dark: #6b6b6b;
    --signature-area: #e2e4ec;
  }
  * { margin: 0; padding: 0; box-sizing: border-box; }
  html, body { width: 1200px; height: 1041px; overflow: hidden; }
  body {
    background: var(--backdrop);
    font-family: "Questrial", "Century Gothic", sans-serif;
    color: var(--ink);
    position: relative;
  }
  .piece { position: absolute; background: var(--paper); overflow: hidden; }

  /* Brand lockup: square + name */
  .brand { position: absolute; display: flex; align-items: center; gap: 7px; }
  .brand-square { background: var(--ink-soft); flex: none; }
  .brand-name {
    text-transform: uppercase; letter-spacing: 0.06em; line-height: 0.95;
    color: var(--ink-soft);
  }
  .brand--light .brand-square { background: #f0f0f0; }
  .brand--light .brand-name { color: #f0f0f0; }

  /* Footer rules */
  .footer-rule { position: absolute; left: 0; right: 0; height: 2px; background: var(--rule-light); }
  .footer-bar { position: absolute; left: 0; right: 0; background: var(--rule-dark); }
  .footer-url {
    position: absolute; background: var(--paper); padding: 0 8px;
    font-size: 6px; letter-spacing: 0.05em; color: var(--ink-soft); text-transform: uppercase;
  }
  .footer-url b { font-weight: 400; color: var(--ink); }

  /* Folder */
  .folder { left: 166px; top: 76px; width: 417px; height: 541px; background: var(--folder); border-radius: 2px; }
  .folder-spine { position: absolute; left: 23px; top: 0; bottom: 0; width: 6px; background: var(--folder-spine); }
  .folder-mark { position: absolute; left: 91px; top: 192px; width: 235px; height: 237px; background: var(--folder-mark); }
  .folder-url {
    position: absolute; left: 0; right: 0; top: 497px; text-align: center;
    font-size: 7.5px; letter-spacing: 0.06em; color: #e2e2e2;
  }
  .folder-url b { font-weight: 400; color: #fff; }

  /* Letterhead */
  .letterhead { left: 615px; top: 95px; width: 403px; height: 523px; }
  .contact-list { position: absolute; font-size: 5.2px; line-height: 7px; color: var(--ink-soft); }
  .contact-list li { list-style: none; display: flex; align-items: center; gap: 3px; }
  .contact-list svg { width: 5px; height: 5px; fill: var(--ink-soft); flex: none; }
  .address { position: absolute; font-size: 5.2px; line-height: 7px; color: var(--ink-soft); }
  .letter-body { position: absolute; left: 37px; top: 156px; width: 330px; font-size: 5.3px; line-height: 7px; text-align: justify; color: var(--ink); }
  .letter-body p { margin-bottom: 7px; }
  .letter-greeting, .signer { font-weight: 700; }
  .letter-closing { margin-top: 6px; }
  .signature { position: absolute; left: 88px; top: 322px; width: 82px; height: 40px; background: var(--signature-area); border-radius: 3px; }

  /* Envelope front */
  .envelope-front { left: 132px; top: 645px; width: 451px; height: 195px; }
  /* Envelope back */
  .envelope-back { left: 615px; top: 645px; width: 451px; height: 195px; }
  .envelope-flap { position: absolute; left: 0; top: 0; width: 451px; height: 65px; }
  .envelope-url { position: absolute; left: 0; right: 0; top: 168px; text-align: center; font-size: 5.5px; color: var(--ink-soft); }

  /* Business cards */
  .card-back { left: 416px; top: 870px; width: 168px; height: 96px; background: var(--folder); }
  .card-back-url { position: absolute; left: 0; right: 0; top: 74px; text-align: center; font-size: 4.2px; color: #e2e2e2; }
  .card-front { left: 615px; top: 870px; width: 167px; height: 96px; }
  .card-name { position: absolute; left: 11px; top: 17px; font-size: 5.3px; font-weight: 700; letter-spacing: 0.04em; color: var(--ink); text-transform: uppercase; }
  .card-role { position: absolute; left: 11px; top: 24px; font-size: 4px; color: var(--ink-soft); }
</style>
</head>
<body>

  <!-- Presentation folder -->
  <section class="piece folder" aria-label="Presentation folder">
    <div class="folder-spine"></div>
    <div class="brand brand--light" style="left:123px; top:57px;">
      <span class="brand-square" style="width:40px; height:40px;"></span>
      <span class="brand-name" style="font-size:19px;">Harbrook<br>Blinds</span>
    </div>
    <div class="folder-mark"></div>
    <p class="folder-url">WWW.<b>HARBROOK</b>.COM</p>
  </section>

  <!-- Letterhead -->
  <section class="piece letterhead" aria-label="Letterhead">
    <div class="brand" style="left:37px; top:31px;">
      <span class="brand-square" style="width:31px; height:31px;"></span>
      <span class="brand-name" style="font-size:14.5px;">Harbrook<br>Blinds</span>
    </div>
    <ul class="contact-list" style="left:309px; top:32px;">
      <li><svg viewBox="0 0 10 10"><path d="M2 1h2l1 2-1.2 1a5 5 0 0 0 2.2 2.2L7 5l2 1v2c0 .6-.4 1-1 1A8 8 0 0 1 1 2c0-.6.4-1 1-1z"/></svg>555.014.3300</li>
      <li><svg viewBox="0 0 10 10"><rect x="1" y="3" width="8" height="5"/><rect x="3" y="1" width="4" height="2"/></svg>555.014.4400</li>
      <li><svg viewBox="0 0 10 10"><rect x="1" y="1" width="8" height="8" rx="1"/></svg>www.harbrook.com</li>
    </ul>
    <p class="address" style="left:309px; top:60px;">1180 Meadow Lane<br>Fairhaven, QLD 4802</p>

    <div class="letter-body">
      <p class="letter-greeting">Dear sir,</p>
      <p>Thank you for choosing our workroom for your recent project. Every order we make is measured, cut and finished by hand at our local factory. Our team has served homes, builders and shopping centres across the region for more than thirty years, and we are proud to keep growing as a family business.</p>
      <p>We would like to confirm the details of your order and the timing of our visit. Our installer will arrive on the agreed morning to check each window, fit the brackets and show you how to care for the fabric. Should you need to change the date, please call our office and we will find a time that suits you. A written quote and a care guide are enclosed with this letter for your records, together with our warranty card and a sample of the chosen fabric.</p>
      <p>We value every client who trusts us with their home or building. Should anything about the finish or fit not meet your needs, let us know and we will put it right without delay. Your feedback helps us keep the standard our customers have come to expect from us.</p>
      <p>Thank you again for your order. We look forward to working with you on this project and on many more in the years ahead. Please keep this letter with your quote and contact us with any questions.</p>
      <p class="letter-closing">Yours Sincerely,<br><span class="signer">Rhea Colton</span></p>
    </div>
    <div class="signature" role="img" aria-label="Handwritten signature of Rhea Colton"></div>

    <div class="footer-rule" style="top:501px;"></div>
    <span class="footer-url" style="left:298px; top:497px;">WWW.<b>HARBROOK</b>.COM</span>
    <div class="footer-bar" style="top:509px; height:6px;"></div>
  </section>

  <!-- Envelope front -->
  <section class="piece envelope-front" aria-label="Envelope front">
    <div class="brand" style="left:22px; top:31px;">
      <span class="brand-square" style="width:31px; height:31px;"></span>
      <span class="brand-name" style="font-size:14.5px;">Harbrook<br>Blinds</span>
    </div>
    <p class="address" style="left:20px; top:80px;">480 Orchard Row<br>Kingsford, QLD 4805</p>
    <div class="footer-rule" style="top:174px;"></div>
    <span class="footer-url" style="left:342px; top:170px;">WWW.<b>HARBROOK</b>.COM</span>
    <div class="footer-bar" style="top:181px; height:6px;"></div>
  </section>

  <!-- Envelope back -->
  <section class="piece envelope-back" aria-label="Envelope back">
    <svg class="envelope-flap" viewBox="0 0 451 65" aria-hidden="true">
      <polygon points="0,0 451,0 433,60 25,60" fill="var(--folder)"/>
    </svg>
    <span class="brand-square" style="position:absolute; left:217px; top:21px; width:19px; height:19px; background:#f0f0f0;"></span>
    <p class="envelope-url">www.harbrook.com</p>
  </section>

  <!-- Business card back -->
  <section class="piece card-back" aria-label="Business card back">
    <div class="brand brand--light" style="left:37px; top:34px;">
      <span class="brand-square" style="width:22px; height:22px;"></span>
      <span class="brand-name" style="font-size:10px;">Harbrook<br>Blinds</span>
    </div>
    <p class="card-back-url">www.harbrook.com</p>
  </section>

  <!-- Business card front -->
  <section class="piece card-front" aria-label="Business card front">
    <p class="card-name">Dale Porter</p>
    <p class="card-role">General Manager</p>
    <div class="brand" style="left:90px; top:15px;">
      <span class="brand-square" style="width:17px; height:17px;"></span>
      <span class="brand-name" style="font-size:8px;">Harbrook<br>Blinds</span>
    </div>
    <ul class="contact-list" style="left:11px; top:61px; font-size:3.8px; line-height:5px;">
      <li><svg viewBox="0 0 10 10" style="width:4px;height:4px;"><path d="M2 1h2l1 2-1.2 1a5 5 0 0 0 2.2 2.2L7 5l2 1v2c0 .6-.4 1-1 1A8 8 0 0 1 1 2c0-.6.4-1 1-1z"/></svg>555.014.3300</li>
      <li><svg viewBox="0 0 10 10" style="width:4px;height:4px;"><rect x="1" y="3" width="8" height="5"/><rect x="3" y="1" width="4" height="2"/></svg>555.014.4400</li>
      <li><svg viewBox="0 0 10 10" style="width:4px;height:4px;"><rect x="1" y="1" width="8" height="8" rx="1"/></svg>www.harbrook.com</li>
    </ul>
    <p class="address" style="left:116px; top:66px; font-size:3.8px; line-height:5px; text-align:right;">1180 Meadow Lane<br>Fairhaven, QLD 4802</p>
    <div class="footer-rule" style="top:82px; height:1.5px;"></div>
    <div class="footer-bar" style="top:86px; height:4px;"></div>
  </section>

</body>
</html>
```